Digital multi-page Product Brochure

We’re creating a product brochure for our Wood Look Porcelain Pavers. The brochure will show technical details of the pavers, available colors, and applications while also showcasing the advantages of porcelain over wood.
We prefer a clean design aesthetic with appropriate white space incorporated. Because we want the view to appreciate the detail and natural look of the porcelain pavers, we want relatively large color swatches in the available colors section.
Each color swatch section needs the information provided in the guide. The design and layout of these sections is completely open. We do want to see a visual of the paver size in each color swatch section along with the written sizing information.
Mixed use of renderings and actual installation photos. Style and placement of photos is up to designer.
Architects and contractors
Building Materials
- Outfit - headers, Helvetica for paragraph copy

```html
<!DOCTYPE html>
<html lang="en">
<head>
<meta charset="utf-8">
<title>Verandek Wood-Look Porcelain Pavers Brochure</title>
<link href="https://fonts.googleapis.com/css2?family=Outfit:wght@400;500;600;700&family=Arimo:wght@400;700&display=swap" rel="stylesheet">
<style>
:root{
  --bg:#a3a3a3;
  --teal:#3aa6c3;
  --teal-dark:#1c8b9c;
  --cyan:#6fd8f0;
  --cyan-light:#a6e8f6;
  --yellow:#f5c518;
  --panel:#eeeeee;
  --cell:#e8e8e8;
  --ink:#2b2b2b;
  --band:#95d0e6;
}
*{margin:0;padding:0;box-sizing:border-box}
html,body{width:1200px;height:3521px;overflow:hidden}
body{background:var(--bg);font-family:Arimo,Helvetica,Arial,sans-serif;color:var(--ink);position:relative}
.abs{position:absolute}
.page{position:absolute;width:490px;height:633px;background:#fff;overflow:hidden}
.heading{position:absolute;left:30px;top:38px;font-family:Outfit,sans-serif;font-weight:600;font-size:17px;color:var(--teal);letter-spacing:.2px}
.copy{position:absolute;left:30px;width:430px;font-size:10px;line-height:1.45;text-align:justify}
.photo{position:absolute}
.footer-brand{position:absolute;left:30px;top:590px;display:flex;align-items:center;gap:5px;font-family:Outfit,sans-serif;font-weight:400;font-size:17px;color:#333}
.footer-brand i{display:block;width:11px;height:11px;background:var(--teal-dark)}
.footer-bar{position:absolute;left:150px;right:0;top:593px;height:13px;background:var(--teal);color:#fff;font-size:8.5px;line-height:13px;padding:0 10px;display:flex;justify-content:space-between}
.tag{position:absolute;background:var(--yellow);font-family:Outfit,sans-serif;font-weight:500;font-size:10.5px;line-height:17px;padding-left:6px;color:#222;white-space:nowrap}
.cover{position:absolute;top:100px;width:440px;height:570px;overflow:hidden}
.back{left:160px;background:var(--teal)}
.front{left:600px;background:#f4f4f4}
.brand-plate{position:absolute;left:50px;top:300px;width:190px;height:44px;background:#fff;display:flex;align-items:center;gap:8px;padding-left:16px;font-family:Outfit,sans-serif;font-size:22px;color:#333}
.brand-plate i{width:14px;height:14px;background:var(--teal-dark);display:block}
.contact{position:absolute;left:50px;color:#fff;font-size:11px;display:flex;align-items:center;gap:10px}
.contact svg{width:20px;height:20px}
.perks{position:absolute;left:30px;top:478px;display:flex;gap:12px}
.perk{width:38px;text-align:center;color:#fff;font-size:6px;line-height:1.2}
.perk b{display:block;width:26px;height:26px;margin:0 auto 4px;border:1.5px solid #fff;border-radius:4px}
.tbl-row{position:absolute;left:30px;width:430px;height:30px;display:flex;gap:0}
.tbl-row .lbl{width:130px;background:var(--cyan);font-size:9px;padding:0 10px;display:flex;align-items:center;line-height:1.1}
.tbl-row .val{flex:1;background:var(--cell);font-size:9px;display:flex;align-items:center;padding-left:50px}
.key{position:absolute;top:72px;width:140px;height:166px;border:1.5px solid var(--cyan-light)}
.key .grid{position:absolute;left:10px;top:8px;display:grid;grid-template-columns:repeat(3,36px);gap:4px}
.key .grid span{height:36px;display:block}
.key .lab{position:absolute;left:0;right:0;bottom:0;height:24px;background:var(--yellow);font-size:9px;line-height:24px;padding-left:10px;white-space:nowrap;overflow:hidden}
.card{position:absolute;left:30px;width:430px;height:102px;background:var(--panel)}
.card .swatch{position:absolute;left:0;top:0;width:97px;height:102px;border:2px solid var(--teal);padding:4px;background:#fff}
.card .swatch span{display:block;width:100%;height:100%}
.card .tag{left:105px;top:4px;width:84px}
.card .size{position:absolute;left:105px;top:34px;font-size:9px;line-height:1.35}
.card .size em{display:inline-block;font-style:normal;background:var(--yellow);padding:0 5px;font-size:8.5px;margin-bottom:2px}
.badge{position:absolute;right:40px;top:62px;width:18px;text-align:center}
.badge .v{display:block;font-size:8px;border:1px solid #555;background:#fff;line-height:11px}
.badge .s{display:block;background:var(--teal);color:#fff;font-size:12px;line-height:19px;margin-top:1px}
.flag{position:absolute;right:14px;top:77px;width:17px;height:17px;border-radius:50%}
.it{background:linear-gradient(90deg,#2f9a43 0 33%,#fff 33% 66%,#d8313a 66%)}
.us{background:linear-gradient(135deg,#2b3f8f 0 35%,transparent 35%),repeating-linear-gradient(180deg,#d8313a 0 3px,#fff 3px 6px)}
</style>
</head>
<body>

<section class="cover back">
  <div class="photo" role="img" aria-label="Rooftop lounge with wood-look porcelain deck and pergola" style="left:0;top:0;width:440px;height:330px;background:linear-gradient(160deg,#7fa6c6 0%,#8a6a4c 45%,#3f342c 100%)"></div>
  <div class="brand-plate"><i></i>Verandek</div>
  <div class="contact" style="top:364px"><svg viewBox="0 0 20 20"><circle cx="10" cy="10" r="9" fill="none" stroke="#fff"/><path d="M7 5l2 3-1 1c1 2 2 3 4 4l1-1 3 2-1 2c-4 0-9-5-9-9z" fill="#fff"/></svg>800 555 0142</div>
  <div class="contact" style="top:392px"><svg viewBox="0 0 20 20"><circle cx="10" cy="10" r="9" fill="none" stroke="#fff"/><rect x="5" y="6.5" width="10" height="7" fill="none" stroke="#fff"/><path d="M5 7l5 4 5-4" fill="none" stroke="#fff"/></svg>hello@verandek.com</div>
  <div class="contact" style="top:420px"><svg viewBox="0 0 20 20"><circle cx="10" cy="10" r="9" fill="none" stroke="#fff"/><circle cx="10" cy="10" r="5" fill="none" stroke="#fff"/><path d="M5 10h10M10 5v10" stroke="#fff"/></svg>www.verandek.com</div>
  <div class="perks">
    <div class="perk"><b></b>Fireproof</div><div class="perk"><b></b>Slip Safe</div><div class="perk"><b></b>Frost Proof</div><div class="perk"><b></b>Low Care</div><div class="perk"><b></b>Scratch Proof</div><div class="perk"><b></b>Stain Proof</div><div class="perk"><b></b>Water Safe</div><div class="perk"><b></b>Easy Install</div>
  </div>
</section>
<section class="cover front">
  <div class="abs" style="right:40px;top:36px;display:flex;align-items:center;gap:8px;font-family:Outfit,sans-serif;font-size:22px;color:#333"><i style="display:block;width:16px;height:16px;background:var(--teal-dark)"></i>Verandek</div>
  <div class="abs" style="left:30px;top:82px;width:380px;height:200px;background:var(--band);border-radius:10px"></div>
  <div class="abs" style="left:48px;top:96px;font-family:Outfit,sans-serif;font-weight:700;font-size:11.5px;color:#222">EVERYTHING YOU NEED TO KNOW ABOUT WOOD-LOOK</div>
  <div class="abs" style="left:56px;top:116px;font-size:8.5px;line-height:1.5;color:#222">• Advantages Over Wood<br>• Colors And Styles<br>• Paver Sizes And Dimensions</div>
  <div class="abs" style="left:240px;top:116px;font-size:8.5px;line-height:1.5;color:#222">• Installation And Laying Options<br>• Project Inspiration</div>
  <div class="photo" role="img" aria-label="City rooftop terrace paved with wood-look porcelain planks" style="left:48px;top:170px;width:344px;height:260px;border-radius:14px;background:linear-gradient(180deg,#9fc0dc 0%,#a98f78 45%,#6a4f3c 100%)"></div>
  <div class="abs" style="left:0;right:0;top:470px;text-align:center;font-family:Outfit,sans-serif;font-weight:700;font-size:30px;color:var(--teal);letter-spacing:1px">PORCELAIN PAVERS</div>
</section>

<section class="page" style="left:94px;top:785px">
  <h2 class="heading">NONCOMBUSTIBLE</h2>
  <p class="copy" style="top:72px">Wood look porcelain pavers used with our Pyrelite Steel Pedestals combine to create a 100% Fireproof decking installation. Fire codes and city requirements are frequently changing.</p>
  <p class="copy" style="top:128px">Our elevated decking system is Class A fire rated.</p>
  <div class="photo" role="img" aria-label="Rendering of white porcelain pavers raised on adjustable steel pedestals" style="left:0;top:175px;width:460px;height:385px;border-radius:0 0 10px 0;background:linear-gradient(160deg,#5b6a7c 0%,#b9c3d3 40%,#e8edf5 70%,#c9d4e6 100%)"></div>
  <svg class="abs" style="left:354px;top:137px" width="82" height="82" viewBox="0 0 82 82">
    <circle cx="41" cy="41" r="39" fill="#fff" stroke="#ddd" stroke-width="2"/>
    <path d="M41 18c6 10 14 14 12 26 0 8-6 14-12 14s-12-6-12-14c0-7 4-10 6-14 1 5 3 7 5 8-2-8 0-14 1-20z" fill="#f28b1e"/>
    <circle cx="41" cy="41" r="28" fill="none" stroke="#d8313a" stroke-width="5"/>
    <line x1="21" y1="21" x2="61" y2="61" stroke="#d8313a" stroke-width="5"/>
  </svg>
  <div class="footer-brand"><i></i>Verandek</div>
  <div class="footer-bar"><span>www.verandek.com</span><span>2</span></div>
</section>

<section class="page" style="left:614px;top:785px">
  <h2 class="heading">THE PORCELAIN ADVANTAGE</h2>
  <p class="copy" style="top:72px;font-size:9.5px">Verandek Wood-Look Porcelain Pavers and Planks beautifully incorporate all the features that make natural wood so appealing, while eliminating the challenges and drawbacks of using wood or <b>composite wood</b> for various projects and installations. <b><i>(It would useful to include composite wood as well I think)</i></b></p>
  <div class="abs" style="left:30px;top:141px;font-size:9.5px;color:var(--teal);font-weight:700">Wood-look Porcelain Pavers vs. Wood</div>
  <div class="abs" style="left:160px;top:172px;width:300px;height:28px;background:var(--cell);font-size:9.5px;display:flex;align-items:center"><span style="width:150px;text-align:center">Wood-look Pavers</span><span style="width:150px;text-align:center">Wood</span></div>
  <div class="tbl-row" style="top:208px"><span class="lbl">Stays cool in the sun</span><span class="val">x</span></div>
  <div class="tbl-row" style="top:244px"><span class="lbl">100% water resistant</span><span class="val">x</span></div>
  <div class="tbl-row" style="top:280px"><span class="lbl">Scratch resistant</span><span class="val">x</span></div>
  <div class="tbl-row" style="top:316px"><span class="lbl">Fireproof</span><span class="val">x</span></div>
  <div class="tbl-row" style="top:352px"><span class="lbl">Low Maintenance</span><span class="val">x</span></div>
  <div class="tbl-row" style="top:388px"><span class="lbl">Fade resistant</span><span class="val">x</span></div>
  <div class="tbl-row" style="top:424px"><span class="lbl">Cold resistant (won't warp or twist)</span><span class="val">x</span></div>
  <div class="tbl-row" style="top:460px"><span class="lbl">On-grade or pedestal supported</span><span class="val">x</span></div>
  <div class="tbl-row" style="top:496px"><span class="lbl">Slip resistant</span><span class="val">x</span></div>
  <div class="tbl-row" style="top:532px"><span class="lbl">Insect resistant</span><span class="val">x</span></div>
  <div class="footer-brand"><i></i>Verandek</div>
  <div class="footer-bar"><span>www.verandek.com</span><span>3</span></div>
</section>

<section class="page" style="left:94px;top:1455px">
  <div class="abs" style="left:0;top:0;width:460px;height:410px;background:var(--panel);border-radius:0 0 10px 0"></div>
  <h2 class="heading">DIMENSIONS AND FEATURES</h2>
  <div class="tag" style="left:0;top:96px;width:70px;padding-left:26px">Slabs</div>
  <div class="photo" role="img" aria-label="Wood-look paver swatch 24 x 24" style="left:30px;top:132px;width:106px;height:93px;background:linear-gradient(90deg,#b06c3e,#c98a58,#a6653a)"></div>
  <div class="tag" style="left:90px;top:211px;width:46px;height:14px;line-height:14px;font-size:8.5px;padding-left:4px">24" x 24"</div>
  <div class="photo" role="img" aria-label="Wood-look paver swatch 24 x 48" style="left:236px;top:132px;width:204px;height:93px;background:linear-gradient(90deg,#6e3f26,#8a5535,#5d3520)"></div>
  <div class="tag" style="left:394px;top:211px;width:46px;height:14px;line-height:14px;font-size:8.5px;padding-left:4px">24" x 48"</div>
  <div class="tag" style="left:0;top:249px;width:80px;padding-left:26px">Planks</div>
  <div class="photo" role="img" aria-label="Plank swatch 8 x 48" style="left:30px;top:283px;width:202px;height:22px;background:linear-gradient(90deg,#f0dcba,#e6cda5)"></div>
  <div class="tag" style="left:186px;top:291px;width:46px;height:14px;line-height:14px;font-size:8.5px;padding-left:4px">8" x 48"</div>
  <div class="photo" role="img" aria-label="Plank swatch 12 x 48" style="left:244px;top:283px;width:202px;height:36px;background:linear-gradient(90deg,#c08950,#d29a62)"></div>
  <div class="tag" style="left:398px;top:305px;width:48px;height:14px;line-height:14px;font-size:8.5px;padding-left:4px">12" x 48"</div>
  <div class="photo" role="img" aria-label="Plank swatch 16 x 48" style="left:30px;top:314px;width:202px;height:50px;background:linear-gradient(90deg,#8a4e2c,#a4623a)"></div>
  <div class="tag" style="left:184px;top:350px;width:48px;height:14px;line-height:14px;font-size:8.5px;padding-left:4px">16" x 48"</div>
  <div class="photo" role="img" aria-label="Plank swatch 10 1/2 x 72" style="left:30px;top:372px;width:264px;height:18px;background:linear-gradient(90deg,#e6c4a4,#dcb58f)"></div>
  <div class="tag" style="left:230px;top:376px;width:64px;height:14px;line-height:14px;font-size:8.5px;padding-left:4px">10 1/2" x 72"</div>
  <div class="abs" style="left:0;top:426px;width:74px;height:28px;background:var(--teal);color:#fff;font-family:Outfit,sans-serif;font-weight:600;font-size:12px;line-height:28px;padding-left:28px">Notes</div>
  <div class="abs" style="left:80px;top:426px;width:380px;height:28px;border:1px solid #999;font-size:9px;line-height:1.2;padding:3px 6px">Nominal sizes may vary by manufacturer. Confirm sizes with Verandek before ordering.</div>
  <div class="abs" style="left:30px;top:477px;font-family:Outfit,sans-serif;font-weight:500;font-size:13px">Variation</div>
  <p class="copy" style="top:503px;font-size:9.5px">Slight tone variations are inherent in porcelain pavers, slabs, and planks. Some colors and styles have minimal variations between each paver and others are significantly distinct from one another. <b>(If we can't pull these from a catalog, <u>we may need to replicate and create our own.</u>)</b></p>
  <div class="footer-brand"><i></i>Verandek</div>
  <div class="footer-bar"><span>www.verandek.com</span><span>4</span></div>
</section>

<section class="page" style="left:614px;top:1455px">
  <h2 class="heading">EXAMPLES FOR KEY</h2>
  <div class="key" style="left:28px"><div class="grid">
    <span style="background:#8a8a8a"></span><span style="background:#b8b8b8"></span><span style="background:#9a9a9a"></span>
    <span style="background:#b0b0b0"></span><span style="background:#bdbdbd"></span><span style="background:#a7a7a7"></span>
    <span style="background:#8f8f8f"></span><span style="background:#b5b5b5"></span><span style="background:#979797"></span>
  </div><div class="lab">V2 - minimal variation</div></div>
  <div class="key" style="left:175px"><div class="grid">
    <span style="background:#5e5e5e"></span><span style="background:#bdbdbd"></span><span style="background:#8a8a8a"></span>
    <span style="background:#c4c4c4"></span><span style="background:#8e8e8e"></span><span style="background:#5a5a5a"></span>
    <span style="background:#6d6d6d"></span><span style="background:#a3a3a3"></span><span style="background:#8c8c8c"></span>
  </div><div class="lab">V3 - moderate variation</div></div>
  <div class="key" style="left:322px"><div class="grid">
    <span style="background:#555"></span><span style="background:#1e1e1e"></span><span style="background:#8a8a8a"></span>
    <span style="background:#1b1b1b"></span><span style="background:#c6c6c6"></span><span style="background:#bbb"></span>
    <span style="background:#d4d4d4"></span><span style="background:#1f1f1f"></span><span style="background:#8e8e8e"></span>
  </div><div class="lab">V4 - significant variation</div></div>
  <svg class="abs" style="left:30px;top:280px" width="430" height="300" viewBox="0 0 430 300" font-family="Outfit, sans-serif">
    <path d="M0 230 A215 215 0 0 1 107.5 43.8 L180 169.4 A70 70 0 0 0 145 230 Z" fill="#1c8b9c" stroke="#fff" stroke-width="4"/>
    <path d="M107.5 43.8 A215 215 0 0 1 322.5 43.8 L250 169.4 A70 70 0 0 0 180 169.4 Z" fill="#3aa6c3" stroke="#fff" stroke-width="4"/>
    <path d="M322.5 43.8 A215 215 0 0 1 430 230 L285 230 A70 70 0 0 0 250 169.4 Z" fill="#1c8b9c" stroke="#fff" stroke-width="4"/>
    <circle cx="215" cy="230" r="64" fill="#fff" stroke="#ddd" stroke-width="3"/>
    <text x="215" y="218" text-anchor="middle" font-size="13" font-weight="600" fill="#3aa6c3">DIMENSIONS</text>
    <text x="215" y="234" text-anchor="middle" font-size="13" font-weight="600" fill="#3aa6c3">AND FEATURES</text>
    <text x="215" y="251" text-anchor="middle" font-size="11" font-weight="600" fill="#1c8b9c">STYLES</text>
    <circle cx="215" cy="17" r="14" fill="#fff" stroke="#3aa6c3" stroke-width="2"/><text x="215" y="22" text-anchor="middle" font-size="14" fill="#3aa6c3">C</text>
    <circle cx="23" cy="150" r="14" fill="#fff" stroke="#1c8b9c" stroke-width="2"/><text x="23" y="155" text-anchor="middle" font-size="14" fill="#1c8b9c">S</text>
    <circle cx="407" cy="150" r="14" fill="#fff" stroke="#1c8b9c" stroke-width="2"/><text x="407" y="155" text-anchor="middle" font-size="14" fill="#1c8b9c">W</text>
    <text x="215" y="72" text-anchor="middle" font-size="12" font-weight="600" fill="#fff">Complex Grain</text>
    <text x="215" y="87" text-anchor="middle" font-size="9" fill="#e6f6fa">Distinct simulated wood</text>
    <text x="215" y="98" text-anchor="middle" font-size="9" fill="#e6f6fa">grain with knots and</text>
    <text x="215" y="109" text-anchor="middle" font-size="9" fill="#e6f6fa">details.</text>
    <text x="50" y="151" font-size="12" font-weight="600" fill="#fff">Straight Grain</text>
    <text x="50" y="164" font-size="9" fill="#e6f6fa">Simple grain pattern</text>
    <text x="50" y="175" font-size="9" fill="#e6f6fa">without prominent</text>
    <text x="50" y="186" font-size="9" fill="#e6f6fa">knots or features.</text>
    <text x="300" y="151" font-size="12" font-weight="600" fill="#fff">Weathered</text>
    <text x="300" y="164" font-size="9" fill="#e6f6fa">Rustic, aged</text>
    <text x="300" y="175" font-size="9" fill="#e6f6fa">look with</text>
    <text x="300" y="186" font-size="9" fill="#e6f6fa">detailed grains.</text>
  </svg>
  <div class="footer-brand"><i></i>Verandek</div>
  <div class="footer-bar"><span>www.verandek.com</span><span>5</span></div>
</section>

<section class="page" style="left:94px;top:2125px">
  <h2 class="heading">COLORS AND STYLES</h2>
  <div class="photo" role="img" aria-label="Modern building with wood-look plank terrace" style="left:30px;top:90px;width:207px;height:140px;border-radius:6px;background:linear-gradient(180deg,#7ea8d4 0%,#3a3f48 45%,#a7785a 100%)"></div>
  <div class="photo" role="img" aria-label="Long plank walkway beside a glass facade and garden" style="left:30px;top:243px;width:207px;height:300px;border-radius:6px;background:linear-gradient(180deg,#5a5f64 0%,#6f7a58 40%,#b07858 100%)"></div>
  <div class="photo" role="img" aria-label="Roof deck with grey pavers, planter and turf" style="left:253px;top:90px;width:207px;height:305px;border-radius:6px;background:linear-gradient(180deg,#aac6e0 0%,#3f7f8a 35%,#a39b92 100%)"></div>
  <div class="photo" role="img" aria-label="Courtyard with wood-look pavers and fire table" style="left:253px;top:408px;width:207px;height:135px;border-radius:6px;background:linear-gradient(180deg,#6b4536 0%,#8a6a52 55%,#5c4a3c 100%)"></div>
  <div class="footer-brand"><i></i>Verandek</div>
  <div class="footer-bar"><span>www.verandek.com</span><span>6</span></div>
</section>

<section class="page" style="left:614px;top:2125px">
  <div class="photo" role="img" aria-label="Rooftop bar seating on large-format wood-look porcelain pavers" style="left:0;top:0;width:415px;height:288px;border-radius:0 0 8px 0;background:linear-gradient(180deg,#b9cbe0 0%,#8c9aa6 40%,#b9a48c 75%,#d3c3ad 100%)"></div>
  <div class="abs" style="left:30px;top:268px;width:180px;height:22px;background:var(--teal);color:#fff;font-family:Outfit,sans-serif;font-weight:600;font-size:12px;line-height:22px;padding-left:4px">COLORS AND STYLES</div>
  <div class="abs" style="left:30px;top:303px;font-family:Outfit,sans-serif;font-weight:500;font-size:13px">Single Boards</div>
  <div class="abs" style="left:30px;top:323px;font-size:9px">One board with singular grain direction.</div>
  <div class="card" style="top:350px;height:108px">
    <div class="swatch" style="height:108px"><span role="img" aria-label="Harborline swatch" style="background:linear-gradient(90deg,#a89c8a,#bcb09c,#9d907c)"></span></div>
    <div class="tag">Harborline 2cm</div>
    <div class="tag" style="left:218px;top:24px;width:28px;font-size:8.5px;line-height:12px">size</div>
    <div class="abs" style="left:218px;top:40px;width:70px;height:24px;background:#fff;border:1px solid #999"></div>
    <div class="abs" style="left:218px;top:66px;width:124px;height:16px;background:#fff;border:1px solid #999"></div>
    <div class="tag" style="left:255px;top:56px;width:32px;height:8px;line-height:8px;font-size:5px;padding-left:3px">24" x 48"</div>
    <div class="tag" style="left:310px;top:72px;width:32px;height:8px;line-height:8px;font-size:5px;padding-left:3px">12" x 48"</div>
    <div class="abs" style="left:366px;top:38px;width:64px;height:64px;border:3px solid #222;background:#fff;padding:4px;display:grid;grid-template-columns:repeat(3,1fr);gap:3px">
      <span style="background:#5e5e5e"></span><span style="background:#bbb"></span><span style="background:#8a8a8a"></span><span style="background:#c4c4c4"></span><span style="background:#8e8e8e"></span><span style="background:#5a5a5a"></span><span style="background:#6d6d6d"></span><span style="background:#a3a3a3"></span><span style="background:#8c8c8c"></span>
    </div>
    <div class="badge" style="left:105px;right:auto;top:62px"><span class="v">V3</span><span class="s">S</span></div>
    <div class="flag us" style="left:130px;right:auto;top:80px"></div>
  </div>
  <div class="card" style="top:468px;height:108px">
    <div class="swatch" style="height:108px"><span role="img" aria-label="Aldermist swatch" style="background:linear-gradient(90deg,#9a8d7e,#ad9f8e,#8e806f)"></span></div>
    <div class="tag">Aldermist 2cm</div>
    <div class="tag" style="left:218px;top:30px;width:28px;font-size:8.5px;line-height:12px">size</div>
    <div class="abs" style="left:218px;top:46px;width:70px;height:24px;background:#fff;border:1px solid #999"></div>
    <div class="abs" style="left:218px;top:72px;width:124px;height:16px;background:#fff;border:1px solid #999"></div>
    <div class="badge" style="left:105px;right:auto;top:62px"><span class="v">V3</span><span class="s">S</span></div>
    <div class="flag us" style="left:130px;right:auto;top:80px"></div>
  </div>
  <div class="footer-brand"><i></i>Verandek</div>
  <div class="footer-bar"><span>www.verandek.com</span><span>7</span></div>
</section>

<section class="page" style="left:94px;top:2798px">
  <div class="card" style="top:31px"><div class="swatch"><span role="img" aria-label="Solvena swatch" style="background:linear-gradient(90deg,#a89a86,#bbae9a,#9c8e7a)"></span></div><div class="tag">Solvena 2cm</div><div class="size"><em>size</em><br>48" x 16"<br>48" x 8"<br>10 1/2" x 72</div><div class="badge"><span class="v">V3</span><span class="s">S</span></div><div class="flag it"></div></div>
  <div class="card" style="top:143px"><div class="swatch"><span role="img" aria-label="Nocella swatch" style="background:linear-gradient(90deg,#a07a55,#b48c64,#946e4b)"></span></div><div class="tag">Nocella 2cm</div><div class="size"><em>size</em><br>48" x 16</div><div class="badge"><span class="v">V4</span><span class="s">S</span></div><div class="flag it"></div></div>
  <div class="card" style="top:255px"><div class="swatch"><span role="img" aria-label="Barleyfield swatch" style="background:linear-gradient(90deg,#9c8f7a,#afa28c,#8f826e)"></span></div><div class="tag">Barleyfield 2cm</div><div class="size"><em>size</em><br>48" x 16</div><div class="badge"><span class="v">V3</span><span class="s">C</span></div><div class="flag it"></div></div>
  <div class="card" style="top:367px"><div class="swatch"><span role="img" aria-label="Terracrest swatch" style="background:linear-gradient(90deg,#7d6a58,#917d69,#705e4d)"></span></div><div class="tag">Terracrest 2cm</div><div class="size"><em>size</em><br>48" x 16"</div><div class="badge"><span class="v">V3</span><span class="s">S</span></div><div class="flag it"></div></div>
  <div class="card" style="top:479px"><div class="swatch"><span role="img" aria-label="Highmoor swatch" style="background:linear-gradient(90deg,#a99478,#bca78a,#9b876c)"></span></div><div class="tag">Highmoor 2cm</div><div class="size"><em>size</em><br>48" x 16 "</div><div class="badge"><span class="v">V3</span><span class="s">W</span></div><div class="flag it"></div></div>
  <div class="footer-brand"><i></i>Verandek</div>
  <div class="footer-bar"><span>www.verandek.com</span><span>8</span></div>
</section>

<section class="page" style="left:614px;top:2798px">
  <div class="card" style="top:31px"><div class="swatch"><span role="img" aria-label="Larchfield swatch" style="background:linear-gradient(90deg,#7b7163,#8e8474,#6f6558)"></span></div><div class="tag">Larchfield 2cm</div><div class="size"><em>size</em><br>48" x 16"</div><div class="badge"><span class="v">V3</span><span class="s">C</span></div><div class="flag it"></div></div>
  <div class="card" style="top:143px"><div class="swatch"><span role="img" aria-label="Shorelyn swatch" style="background:linear-gradient(90deg,#aaa8a2,#bdbbb5,#9e9c96)"></span></div><div class="tag">Shorelyn 2cm</div><div class="size"><em>size</em><br>12" x 47 "<br>24" x 48"</div><div class="badge"><span class="v">V3</span><span class="s">W</span></div><div class="flag us"></div></div>
  <div class="card" style="top:255px"><div class="swatch"><span role="img" aria-label="Aldermist swatch" style="background:linear-gradient(90deg,#8c7b69,#a08e7a,#80705f)"></span></div><div class="tag">Aldermist 2cm</div><div class="size"><em>size</em><br>12 x 48"<br>24" x 48"</div><div class="badge"><span class="v">V3</span><span class="s">C</span></div><div class="flag us"></div></div>
  <div class="card" style="top:367px"><div class="swatch"><span role="img" aria-label="Ebonvale swatch" style="background:linear-gradient(90deg,#5e5046,#706157,#54473e)"></span></div><div class="tag">Ebonvale 2cm</div><div class="size"><em>size</em><br>47" x 15 5/8"</div><div class="badge"><span class="v">V3</span><span class="s">C</span></div><div class="flag it"></div></div>
  <div class="card" style="top:479px"><div class="swatch"><span role="img" aria-label="Redgrove swatch" style="background:linear-gradient(90deg,#8a5c47,#9e6d56,#7d513e)"></span></div><div class="tag">Redgrove 2cm</div><div class="size"><em>size</em><br>47" x 15 5/8"</div><div class="badge"><span class="v">V3</span><span class="s">C</span></div><div class="flag it"></div></div>
  <div class="footer-brand"><i></i>Verandek</div>
  <div class="footer-bar"><span>www.verandek.com</span><span>9</span></div>
</section>

</body>
</html>
```